Business Card Design

Rolf Quenby Insurance Agency, an Independent Insurance Agency which was stated on Harlow Lane in Laplace, Louisiana on 1958 and has grown the six locations throughout South Louisiana. We sell personal (auto Homeowners flood, liability) and commercial insurance (commercial property, general liability, workers compensation, commercial auto). I am looking for a double sided card with list the five remaining locations on the back or maybe even a folded four sided card. Our home office is a two story building with a green roof. I have had a logo designed which I have attached. Open for revisions but would like to stay with in the same green roof over an M. I have attached the logo but can not tell if I was uploaded.

Target Market(s)

Individual and commercial insurance buyers. Upper income and business owners

Industry/Entity Type

Insurance

Requirements
Must have
• Must have similar logo as uploaded. Green roof over M or something similar. List all location address and phone numbers.

Employee name, office phone number; direct phone line; email address and website list all locations on card. Very Similar colors to current logo.
Nice to have
• Possible folded card with double sided print

```html
<!DOCTYPE html>
<html lang="en">
<head>
<meta charset="utf-8">
<title>Rolf Quenby Insurance Agency – Stationery</title>
<link rel="stylesheet" href="https://fonts.googleapis.com/css2?family=Arimo:ital,wght@0,400;0,700;1,400;1,700&display=swap">
<style>
:root{
  --green:#1d5a2e;
  --blue:#1a73c4;
  --ink:#333;
  --paper:#fff;
  --stage:#d9d9d9;
  --rule:#9fc3e6;
  --row:#eef2f6;
}
*{margin:0;padding:0;box-sizing:border-box}
html,body{width:960px;height:1200px;overflow:hidden}
body{background:var(--stage);font-family:"Arimo",Arial,sans-serif;color:var(--ink);position:relative}
.sheet{position:absolute;background:var(--paper);overflow:hidden;box-shadow:0 1px 4px rgba(0,0,0,.25)}
.letterhead{left:36px;top:30px;width:422px;height:547px}
.fax{left:36px;top:638px;width:422px;height:547px}
.brand{position:absolute;left:46px;top:32px;color:var(--green);display:flex;align-items:flex-start;gap:6px}
.brand-mark{width:14px;height:14px;background:var(--green);margin-top:2px}
.brand-name{font-weight:700;font-size:11.5px;line-height:12px;text-transform:uppercase}
.brand-tag{font-weight:700;font-size:6px;line-height:8px}
.contacts{position:absolute;left:258px;top:28px;list-style:none;font-size:8.4px;line-height:10.6px}
.contacts li{display:flex;align-items:center;gap:6px}
.contacts svg{width:8px;height:8px;fill:var(--blue)}
.letter{position:absolute;left:46px;top:110px;width:330px;font-size:6.3px;line-height:8.6px;color:#444}
.letter p{margin-bottom:8.6px}
.signature{width:110px;height:24px;background:linear-gradient(90deg,#e6eef8,#f4f7fb);margin-top:4px}
.footer-band{position:absolute;left:0;bottom:0;width:100%;height:58px}
.footer-address{position:absolute;right:24px;bottom:6px;color:#fff;font-size:6.6px;line-height:8.4px;text-align:right}
.cover{position:absolute;left:517px;top:30px;width:422px;height:547px;background:linear-gradient(160deg,#2f93e6,#146bc0 70%,#1a74c8);color:#fff;box-shadow:0 1px 4px rgba(0,0,0,.25)}
.cover-brand{position:absolute;left:108px;top:84px;display:flex;gap:8px}
.cover-brand .brand-mark{width:28px;height:28px;background:#fff;margin-top:2px}
.cover-name{font-weight:700;font-size:17px;line-height:17px;text-transform:uppercase}
.cover-tag{font-weight:700;font-size:9.5px;margin-top:1px}
.cover-credit{position:absolute;left:0;top:427px;width:100%;text-align:center;text-transform:uppercase}
.cover-credit .label{font-size:12px;letter-spacing:.5px}
.cover-credit .person{font-weight:700;font-size:18px;line-height:20px}
.cover-credit .agency{font-size:11.5px}
.fax-title{position:absolute;left:0;top:93px;width:100%;text-align:center;color:var(--blue);font-weight:700;font-style:italic;font-size:12.5px}
.fax-table{position:absolute;left:27px;top:125px;width:370px;border-collapse:collapse;font-size:7.4px;border:1px dashed var(--rule)}
.fax-table td{height:15.5px;padding:0 6px;border-bottom:1px dashed var(--rule)}
.fax-table tr:nth-child(odd){background:var(--row)}
.fax-table th{text-align:left;color:var(--blue);font-weight:700;padding-left:8px;width:46px}
.fax-table td{font-style:italic;color:#555}
.fax-table .split{border-right:1px dashed var(--rule)}
.fax-fields{position:absolute;left:30px;top:220px;width:370px;font-size:7.7px;line-height:10.5px;color:#444}
.field{display:flex;margin-bottom:10px}
.field dt{width:79px;flex:none;color:var(--blue);font-weight:700}
.card{position:absolute;width:225px;height:128px;overflow:hidden;box-shadow:0 1px 3px rgba(0,0,0,.25)}
.card-front{left:517px;top:637px;background:var(--paper)}
.card-back{background:linear-gradient(160deg,#3a96e6,#1668bd);color:#fff}
.card-back-a{left:517px;top:783px}
.card-back-b{left:517px;top:935px}
.card .brand{left:20px;top:14px;gap:4px}
.card .brand-mark{width:8px;height:8px}
.card .brand-name{font-size:7px;line-height:7.4px}
.card .brand-tag{font-size:4px;line-height:5px}
.card-person{position:absolute;left:162px;top:54px;color:var(--blue);font-weight:700;font-size:7.4px}
.card-lines{position:absolute;left:20px;top:52px;font-size:5.2px;line-height:6.6px;color:var(--blue);list-style:none}
.card-lines li{display:flex;gap:4px;align-items:flex-start}
.card-lines svg{width:5px;height:5px;fill:var(--blue);margin-top:1px}
.card-lines .gap{height:6px}
.card-web{position:absolute;right:14px;bottom:5px;color:#fff;font-size:5px}
.locations{position:absolute;display:grid;grid-template-columns:88px 88px;row-gap:9px;font-size:5px;line-height:6.4px}
.card-back-a .locations{left:48px;top:19px}
.card-back-b .locations{left:18px;top:18px;grid-template-columns:113px 88px}
.vertical-name{position:absolute;left:8px;top:118px;transform:rotate(-90deg);transform-origin:left top;font-weight:700;font-size:8px;line-height:8.4px;text-transform:uppercase;white-space:nowrap}
.vertical-name small{display:block;font-size:4.2px;line-height:5px;text-transform:none}
.back-rule{position:absolute;left:48px;right:50px;top:116px;height:0;border-top:1px solid rgba(255,255,255,.8)}
.card-back-a .card-web{bottom:4px}
.divider{position:absolute;left:111px;top:16px;height:100px;border-left:1px solid rgba(255,255,255,.8)}
.back-brand{position:absolute;left:125px;top:90px;display:flex;gap:4px}
.back-brand .brand-mark{width:10px;height:10px;background:#fff}
.back-brand .brand-name{font-size:7px;line-height:7.4px;font-weight:700;text-transform:uppercase}
.back-brand .brand-tag{font-size:4px;font-weight:700}
</style>
</head>
<body>

<section class="sheet letterhead">
  <div class="brand">
    <span class="brand-mark"></span>
    <div><div class="brand-name">Rolf Quenby<br>Insurance Agency</div><div class="brand-tag">Your Harlow Lane Neighbors</div></div>
  </div>
  <ul class="contacts">
    <li><svg viewBox="0 0 10 10"><path d="M1 3h8v5H1zM3 1h4v2H3z"/></svg>225-555-0142 (Direct)</li>
    <li><svg viewBox="0 0 10 10"><path d="M2 1l2 2-1 1.5c.7 1.3 1.3 2 2.5 2.5L7 6l2 2-1.5 1.5C4 9 1 6 .5 2.5z"/></svg>985-555-0178 (Office)</li>
    <li><svg viewBox="0 0 10 10"><path d="M0 2h10v6H0zM0 2l5 3.5L10 2"/></svg>nora.pellan@rolfquenby.com</li>
    <li><svg viewBox="0 0 10 10"><circle cx="5" cy="5" r="4.5"/></svg>www.rolfquenby.com</li>
  </ul>
  <div class="letter">
    <p>Dear Alan,</p>
    <p>Lorem ipsum dolor sit amet, consectetuer adipiscing elit, sed diam nonummy nibh euismod tincidunt ut laoreet dolore magna aliquam erat volutpat. Ut wisi enim ad minim veniam, quis nostrud exerci tation ullamcorper suscipit lobortis nisl ut aliquip ex ea commodo consequat. Duis dolore te feugait nulla facilisi. Nam liber tempor cum soluta nobis eleifend option congue nihil imperdiet doming id quod mazim placerat facer possim assum.</p>
    <p>Duis autem vel eum iriure dolor in hendrerit in vulputate velit esse molestie consequat, vel illum dolore eu feugiat nulla facilisis at vero eros et accumsan et iusto odio dignissim qui blandit praesent luptatum zzril delenit augue duis dolore te feugait nulla facilisi. Consectetuer adipiscing elit, sed diam nonummy nibh euismod tincidunt ut laoreet dolore magna aliquam erat volutpat. Ut wisi enim ad minim veniam, quis nostrud exerci tation ullamcorper suscipit lobortis nisl ut aliquip ex ea commodo consequat.</p>
    <p>Consectetuer adipiscing elit, sed diam nonummy nibh euismod tincidunt ut laoreet dolore magna aliquam erat volutpat. Ut wisi enim ad minim veniam, quis nostrud exerci tation ullamcorper suscipit lobortis nisl ut aliquip ex ea commodo consequat. Consectetuer adipiscing elit, sed diam nonummy nibh euismod tincidunt ut laoreet dolore magna aliquam erat volutpat. Ut wisi enim ad minim veniam, quis nostrud exerci tation ullamcorper suscipit lobortis nisl ut aliquip ex ea commodo consequat.</p>
    <p>Dolor sit amet, consectetuer adipiscing elit, sed diam nonummy nibh euismod tincidunt ut laoreet dolore magna aliquam erat volutpat. Ut wisi enim ad minim veniam, quis nostrud exerci tation ullamcorper suscipit lobortis nisl ut aliquip ex ea commodo consequat. Duis dolore te feugait nulla facilisi. Nam liber tempor cum soluta nobis eleifend option congue nihil imperdiet doming id quod mazim placerat facer possim assum. Duis dolore te feugait nulla facilisi. Nam liber tempor cum soluta nobis eleifend option congue nihil imperdiet doming id quod mazim placerat facer possim assum.</p>
    <p style="margin-bottom:2px">Sincerely,</p>
    <div class="signature" role="img" aria-label="Handwritten signature"></div>
  </div>
  <svg class="footer-band" viewBox="0 0 422 58" preserveAspectRatio="none">
    <path d="M0 22 C120 4 300 4 422 18 L422 58 L0 58Z" fill="var(--green)"/>
    <path d="M0 58 L0 44 C110 24 300 20 422 24 L422 58Z" fill="var(--blue)"/>
  </svg>
  <div class="footer-address">Rolf Quenby Insurance Agency<br>418 North Alder, Suite 3 Ponchatoula, LA 70454</div>
</section>

<section class="cover">
  <div class="cover-brand">
    <span class="brand-mark"></span>
    <div><div class="cover-name">Rolf Quenby<br>Insurance Agency</div><div class="cover-tag">Your Harlow Lane Neighbors</div></div>
  </div>
  <div class="cover-credit">
    <div class="label">Directed by</div>
    <div class="person">Nora Pellan</div>
    <div class="agency">Rolf Quenby Insurance Agency</div>
  </div>
</section>

<section class="sheet fax">
  <div class="brand">
    <span class="brand-mark"></span>
    <div><div class="brand-name">Rolf Quenby<br>Insurance Agency</div><div class="brand-tag">Your Harlow Lane Neighbors</div></div>
  </div>
  <ul class="contacts" style="top:20px">
    <li><svg viewBox="0 0 10 10"><path d="M1 3h8v5H1zM3 1h4v2H3z"/></svg>225-555-0142 (Direct)</li>
    <li><svg viewBox="0 0 10 10"><path d="M2 1l2 2-1 1.5c.7 1.3 1.3 2 2.5 2.5L7 6l2 2-1.5 1.5C4 9 1 6 .5 2.5z"/></svg>985-555-0178 (Office)</li>
    <li><svg viewBox="0 0 10 10"><path d="M0 2h10v6H0zM0 2l5 3.5L10 2"/></svg>nora.pellan@rolfquenby.com</li>
    <li><svg viewBox="0 0 10 10"><circle cx="5" cy="5" r="4.5"/></svg>www.rolfquenby.com</li>
  </ul>
  <h1 class="fax-title">Facsimile Transmittal</h1>
  <table class="fax-table">
    <tr><th>Subject</th><td class="split">: Your subject should be here</td><th>Date</th><td>: 25/01/2015</td></tr>
    <tr><th>To</th><td class="split">: Customer Company/Name Here</td><th>From</th><td>: Rolf Quenby Insurance Agency</td></tr>
    <tr><th>Cc</th><td class="split">: Customer Company/Name Here</td><th>Phone</th><td>: 985-555-0178</td></tr>
    <tr><th>Fax</th><td class="split">: Type Fax Number</td><th>Fax</th><td>: 985-555-0178</td></tr>
  </table>
  <dl class="fax-fields">
    <div class="field"><dt>Action Required :</dt><dd>Lorem ipsum dolor sit amet, consectetuer adipiscing elit, sed diam nonummy nibh euismod tincidunt ut laoreet.</dd></div>
    <div class="field"><dt>Recomendation :</dt><dd>Lorem ipsum dolor sit amet, consectetuer adipiscing elit, sed diam nonummy nibh euismod tincidunt ut laoreet dolore magna aliquam erat volutpat. Ut wisi enim ad minim veniam.</dd></div>
    <div class="field"><dt>Background :</dt><dd>Lorem ipsum dolor sit amet, consectetuer adipiscing elit, sed diam nonummy nibh euismod tincidunt ut laoreet dolore magna aliquam erat volutpat. Ut wisi enim ad minim veniam, quis nostrud exerci tation ullamcorper suscipit lobortis nisl ut aliquip ex ea commodo consequat. Duis autem vel eum iriure dolor in hendrerit in vulputate velit esse molestie consequat, vel illum dolore eu feugiat nulla facilisis at vero eros et accumsan et iusto odio dignissim qui blandit praesent luptatum zzril delenit augue duis dolore te feugait nulla facilisi. Nam liber tempor cum soluta nobis eleifend option congue nihil imperdiet doming id quod mazim placerat facer possim assum. Typi non habent claritatem insitam; est usus legentis in iis qui facit eorum claritatem. Investigationes demonstraverunt lectores legere me lius quod ii legunt saepius. Claritas est etiam processus dynamicus, qui sequitur mutationem consuetudium lectorum. Mirum est notare quam littera gothica, quam nunc</dd></div>
    <div class="field"><dt>Attachment :</dt><dd>Lorem ipsum, dolor sit amet, consectetuer, adipiscing elit, Invoice.</dd></div>
  </dl>
  <svg class="footer-band" viewBox="0 0 422 58" preserveAspectRatio="none">
    <path d="M0 22 C120 4 300 4 422 18 L422 58 L0 58Z" fill="var(--green)"/>
    <path d="M0 58 L0 44 C110 24 300 20 422 24 L422 58Z" fill="var(--blue)"/>
  </svg>
  <div class="footer-address">Rolf Quenby Insurance Agency<br>418 North Alder, Suite 3 Ponchatoula, LA 70454</div>
</section>

<section class="card card-front">
  <div class="brand">
    <span class="brand-mark"></span>
    <div><div class="brand-name">Rolf Quenby<br>Insurance Agency</div><div class="brand-tag">Your Harlow Lane Neighbors</div></div>
  </div>
  <div class="card-person">NORA PELLAN</div>
  <ul class="card-lines">
    <li><svg viewBox="0 0 10 10"><circle cx="5" cy="4" r="3.5"/><path d="M2 6l3 4 3-4z"/></svg><span>Rolf Quenby Insurance Agency<br>418 North Alder<br>Suite 3 Ponchatoula, LA 70454</span></li>
    <li class="gap"></li>
    <li><svg viewBox="0 0 10 10"><path d="M1 3h8v5H1zM3 1h4v2H3z"/></svg>225-555-0142 (Direct)</li>
    <li><svg viewBox="0 0 10 10"><path d="M2 1l2 2-1 1.5c.7 1.3 1.3 2 2.5 2.5L7 6l2 2-1.5 1.5C4 9 1 6 .5 2.5z"/></svg>985-555-0178 (Office)</li>
    <li><svg viewBox="0 0 10 10"><path d="M0 2h10v6H0z"/></svg>nora.pellan@rolfquenby.com</li>
  </ul>
  <svg class="footer-band" style="height:26px" viewBox="0 0 225 26" preserveAspectRatio="none">
    <path d="M0 12 C60 2 160 0 225 6 L225 26 L0 26Z" fill="var(--green)"/>
    <path d="M0 26 L0 22 C60 12 160 10 225 12 L225 26Z" fill="var(--blue)"/>
  </svg>
  <div class="card-web">www.rolfquenby.com</div>
</section>

<section class="card card-back card-back-a">
  <div class="vertical-name">Rolf Quenby<br>Insurance Agency<small>Your Harlow Lane Neighbors</small></div>
  <div class="locations">
    <div>Rolf Quenby Insurance Agency<br>418 North Alder<br>Suite 3 Ponchatoula, LA 70454</div>
    <div>Rolf Quenby Insurance Agency<br>418 North Alder<br>Suite 3 Ponchatoula, LA 70454</div>
    <div>Rolf Quenby Insurance Agency<br>418 North Alder<br>Suite 3 Ponchatoula, LA 70454</div>
    <div>Rolf Quenby Insurance Agency<br>418 North Alder<br>Suite 3 Ponchatoula, LA 70454</div>
    <div>Rolf Quenby Insurance Agency<br>418 North Alder<br>Suite 3 Ponchatoula, LA 70454</div>
  </div>
  <div class="back-rule"></div>
  <div class="card-web">www.rolfquenby.com</div>
</section>

<section class="card card-back card-back-b">
  <div class="locations">
    <div>Rolf Quenby Insurance Agency<br>418 North Alder<br>Suite 3 Ponchatoula, LA 70454</div>
    <div>Rolf Quenby Insurance Agency<br>418 North Alder<br>Suite 3 Ponchatoula, LA 70454</div>
    <div>Rolf Quenby Insurance Agency<br>418 North Alder<br>Suite 3 Ponchatoula, LA 70454</div>
    <div>Rolf Quenby Insurance Agency<br>418 North Alder<br>Suite 3 Ponchatoula, LA 70454</div>
    <div>Rolf Quenby Insurance Agency<br>418 North Alder<br>Suite 3 Ponchatoula, LA 70454</div>
  </div>
  <div class="divider"></div>
  <div class="back-brand">
    <span class="brand-mark"></span>
    <div><div class="brand-name">Rolf Quenby<br>Insurance Agency</div><div class="brand-tag">Your Harlow Lane Neighbors</div></div>
  </div>
</section>

</body>
</html>
```